MAREK DOLVANE FOR CONGRESS DISTRICT 32

I need to create a campaign flyer for my congress campaign. I am running for congress in District 32 of Texas as a republican. I am a former Olympic athlete, world champion fencer, Army veteran, Counterintelligence officer (I catch spies).
I want just my first name MAREK in big letters at the top. I want it to say MAREK and below it Republican for Congress.
www.marekforcongress.example

Industry/Entity Type

Political

Colors
EB3D1F
EC4F4E
F09395
F8D3D4
FCEDEE

Requirements
Nice to have
• Would love a catchy title for the Flyer like "Spy Catcher", "Olympic Athlete" "World Champion Fencer" running for Congress in your District!

```html
<!DOCTYPE html>
<html lang="en">
<head>
<meta charset="utf-8">
<title>Marek Dolvane for Congress</title>
<link rel="stylesheet" href="https://fonts.googleapis.com/css2?family=Josefin+Sans:wght@600;700&family=Lexend:wght@600&family=Montserrat:wght@800;900&display=swap">
<style>
  :root {
    --navy: #1a2256;
    --navy-deep: #131a45;
    --royal: #26357a;
    --red: #b0101c;
    --red-bright: #cc0a22;
    --white: #ffffff;
    --paper: #f3f3f7;
    --star-red: #c8202c;
  }
  * { margin: 0; padding: 0; box-sizing: border-box; }
  html, body { width: 927px; height: 1200px; overflow: hidden; background: var(--navy); }
  .flyer { position: relative; width: 927px; height: 1200px; overflow: hidden;
    background: linear-gradient(180deg, var(--red) 0%, #8e0c1c 30%, #3c1a4e 50%, var(--navy) 62%, var(--navy-deep) 100%); }
  .backdrop { position: absolute; inset: 0; }
  .portrait { position: absolute; left: 272px; top: 190px; width: 379px; height: 392px;
    background: linear-gradient(180deg, #9a9a9a 0%, #7a7a76 45%, rgba(90,90,100,0.5) 80%, rgba(40,45,90,0) 100%);
    clip-path: polygon(33% 0, 67% 0, 72% 38%, 100% 52%, 100% 100%, 0 100%, 0 52%, 28% 38%); }
  .headline { position: absolute; left: 0; top: 0; width: 927px; height: 1200px; }
  .first-name { font-family: "Lexend", sans-serif; font-weight: 600; fill: var(--white); }
  .tagline { font-family: "Josefin Sans", sans-serif; font-weight: 700; fill: var(--white); }
  .info-box { position: absolute; left: 157px; top: 794px; width: 613px; height: 178px;
    border: 1.5px solid var(--white); clip-path: polygon(0 0, 100% 0, 100% 92%, 97.8% 100%, 0 100%); }
  .site { height: 54px; background: var(--paper); display: flex; align-items: center; justify-content: center;
    padding-top: 4px; white-space: nowrap; overflow: hidden;
    font-family: "Josefin Sans", sans-serif; font-weight: 700; font-size: 27px; color: var(--royal); letter-spacing: 0; }
  .credentials { display: flex; height: 124px; }
  .credentials ul { list-style: none; flex: 1; padding: 20px 0 0 14px; }
  .credentials ul + ul { border-left: 1.5px solid var(--white); }
  .credentials li { position: relative; padding-left: 26px; margin-bottom: 14px;
    font-family: "Josefin Sans", sans-serif; font-weight: 700; font-size: 20px; line-height: 24px;
    letter-spacing: 1px; color: var(--white); }
  .credentials li svg { position: absolute; left: 0; top: 1px; width: 20px; height: 20px; fill: var(--star-red); }
  .sign-off { position: absolute; left: 250px; top: 1003px; display: flex; align-items: center; gap: 12px; }
  .sign-off .name { font-family: "Montserrat", sans-serif; font-weight: 900; font-size: 34px; line-height: 38px; color: var(--white); letter-spacing: -0.5px; }
  .sign-off .district { font-family: "Montserrat", sans-serif; font-weight: 900; font-size: 18px; line-height: 22px; color: var(--white); }
  .sign-off .mark { width: 30px; height: 30px; background: var(--white); }
</style>
</head>
<body>
<main class="flyer">
  <svg class="backdrop" width="927" height="1200" viewBox="0 0 927 1200">
    <defs>
      <linearGradient id="drape-blue" x1="0" y1="0" x2="1" y2="1">
        <stop offset="0" stop-color="#1e2a6c"/>
        <stop offset="1" stop-color="#15205a"/>
      </linearGradient>
    </defs>
    <polygon role="img" aria-label="Draped flag canton with white stars" points="0,0 272,0 0,850" fill="url(#drape-blue)"/>
    <polygon class="stripe-red" points="672,0 927,0 927,730" fill="var(--red-bright)"/>
    <polygon class="stripe-white" points="757,0 840,0 927,340 927,440" fill="var(--white)"/>
  </svg>

  <div class="portrait" role="img" aria-label="Candidate portrait in Army uniform"></div>

  <svg class="headline" width="927" height="1200" viewBox="0 0 927 1200">
    <text class="first-name" x="157" y="711" font-size="245" textLength="614" lengthAdjust="spacingAndGlyphs">MAREK</text>
    <text class="tagline" x="157" y="763" font-size="41" textLength="613" lengthAdjust="spacingAndGlyphs">REPUBLICAN FOR CONGRESS</text>
  </svg>

  <section class="info-box">
    <div class="site">WWW.MAREKFORCONGRESS.EXAMPLE</div>
    <div class="credentials">
      <ul>
        <li><svg viewBox="0 0 24 24"><path d="M12 1l3.1 7.6 8.2.6-6.3 5.3 2 8-7-4.4-7 4.4 2-8L.7 9.2l8.2-.6z"/></svg>OLYMPIC ATHLETE</li>
        <li><svg viewBox="0 0 24 24"><path d="M12 1l3.1 7.6 8.2.6-6.3 5.3 2 8-7-4.4-7 4.4 2-8L.7 9.2l8.2-.6z"/></svg>WORLD CHAMPION<br>FENCER</li>
      </ul>
      <ul>
        <li><svg viewBox="0 0 24 24"><path d="M12 1l3.1 7.6 8.2.6-6.3 5.3 2 8-7-4.4-7 4.4 2-8L.7 9.2l8.2-.6z"/></svg>ARMY VETERAN</li>
        <li><svg viewBox="0 0 24 24"><path d="M12 1l3.1 7.6 8.2.6-6.3 5.3 2 8-7-4.4-7 4.4 2-8L.7 9.2l8.2-.6z"/></svg>COUNTERINTELLIGENCE<br>OFFICER</li>
      </ul>
    </div>
  </section>

  <footer class="sign-off">
    <div>
      <div class="name">MAREK DOLVANE</div>
      <div class="district">FOR CONGRESS TEXAS-32</div>
    </div>
    <div class="mark"></div>
  </footer>
</main>
</body>
</html>
```